8 Page Publishing/Entertainment Website Design

We need a slick, polished, professional looking fully mobile responsive website designed for the publishing / entertainment industry. It will contain 8 pages, including the Home page. The site is to be designed in pure HTML and CSS only and to be compatible with any type of server we put it on. Pages are *not* to be part of any template system, like WordPress or others like it. Pure HTML and CSS standalone pages only. No WordPress or Joomla, etc. Website to use our logo's colors of red/white throughout its design. Uploaded files contain a word DOC that outlines more of our needs and we have included our logo file. Please read the specifications in the Word Document attached. We have also included a PDF file with the website specs as well.

Target Market(s)

Authors and Screenwriters

Coding

Coded - Design and coding required

Number of Pages Required

5+ page

Colors
ec1f27
ffffff
f04a50
f59195

Requirements
Must have
• The site is to be designed in pure HTML and CSS only and to be compatible with any type of server we put it on. Pages are *not* to be part of any template system, like WordPress or others like it. Pure HTML and CSS standalone pages only. No WordPress or Joomla, etc. Website to use our logo's colors of red/white throughout its design. Uploaded files contain a word DOC that outlines more of our needs and we have included our logo file. Please read the specifications in the Word Document attached. We have also included a PDF file with the website specs as well.
Should not have
• No Wordpress or other Template type pages. Pure HTML and CSS only. Some Javascript and JQuery is okay, upon approval.

```html
<!DOCTYPE html>
<html lang="en">
<head>
<meta charset="utf-8">
<title>Beacon Point Publishing</title>
<link href="https://fonts.googleapis.com/css2?family=Poppins:wght@300;400;500;600;700&display=swap" rel="stylesheet">
<style>
:root{
  --red:#ec1f27;
  --red-soft:#f04a50;
  --red-pale:#f59195;
  --white:#ffffff;
  --dark:#3a3a3a;
  --ink:#2b2b2b;
  --text:#555555;
  --grey-bg:#f1f1f1;
}
*{margin:0;padding:0;box-sizing:border-box}
html,body{width:1200px;height:3015px;overflow:hidden}
body{font-family:'Poppins',sans-serif;color:var(--text);background:var(--white);position:relative}
.abs{position:absolute}

/* header */
.site-header{left:0;top:0;width:1200px;height:75px;background:var(--dark);z-index:2}
.brand{left:0;top:0;width:365px;height:75px;background:var(--red);display:flex;align-items:center;padding-left:86px;gap:12px}
.brand-dot{width:34px;height:34px;border-radius:50%;background:var(--white)}
.brand-name{color:var(--white);font-weight:600;font-size:15px;letter-spacing:.2px}
.main-nav{right:86px;top:0;height:75px;display:flex;align-items:center;gap:24px}
.main-nav a{color:var(--white);text-decoration:none;font-size:14.5px;font-weight:300}

/* hero */
.hero{left:0;top:75px;width:1200px;height:473px;background:linear-gradient(90deg,#f4f2f0 0%,#ece7e2 55%,#e2d3bf 74%,#d6a77a 86%,#e6d8c6 100%)}
.hero-title{left:178px;top:110px;font-size:33px;font-weight:700;color:var(--ink);letter-spacing:.5px;line-height:46px;z-index:2}
.hero-video{left:86px;top:172px;width:562px;height:272px;background:linear-gradient(135deg,#2a2d33,#45403a 60%,#1e2024)}
.play{left:242px;top:98px;width:78px;height:78px}
.hero-apply{left:86px;top:444px;width:562px;height:56px;background:var(--red);color:var(--white);font-weight:600;font-size:21px;display:flex;align-items:center;justify-content:center}

/* section titles */
.sec-title{font-size:30px;font-weight:700;color:var(--red);text-transform:uppercase}
.rule{width:90px;height:2px;background:var(--ink)}
.center{left:0;width:1200px;text-align:center}

/* about */
.about-title{left:84px;top:626px}
.about-rule{left:86px;top:674px}
.about-text{left:86px;top:688px;width:1030px;font-size:13px;line-height:25px}
.more{color:var(--red);text-decoration:underline;font-size:12px}

/* worlds */
.worlds{left:0;top:842px;width:1200px;height:436px;background:var(--grey-bg)}
.worlds-img{left:0;top:0;width:704px;height:436px;background:linear-gradient(105deg,#c9733f 0%,#eab27c 30%,#f4dcc0 48%,#e9b585 68%,#b9542f 100%)}
.worlds-box{left:668px;top:62px;width:532px;height:312px;background:var(--red);box-shadow:0 10px 24px rgba(0,0,0,.25);padding:50px 86px 0 86px;color:var(--white)}
.worlds-box h2{font-size:30px;font-weight:700}
.worlds-box .rule{background:var(--ink);margin:6px 0 18px}
.worlds-box p{font-size:13.4px;line-height:25px}
.btn-white{display:flex;align-items:center;justify-content:center;width:218px;height:38px;background:var(--white);color:var(--red);font-weight:600;font-size:15px;margin-top:24px}

/* authors */
.authors-title{top:1354px}
.authors-rule{left:555px;top:1404px}
.author{top:1443px;width:237px;height:309px}
.author-photo{background:linear-gradient(180deg,#6b7076,#8a8478 50%,#4c5057)}
.author-name{left:0;bottom:0;width:237px;height:42px;background:rgba(30,30,30,.85);color:var(--white);font-size:15px;display:flex;align-items:center;justify-content:center}
.author-featured{background:var(--red-soft);color:var(--white);text-align:center;padding:60px 26px 0}
.author-featured h3{font-size:20px;font-weight:500;margin-bottom:4px}
.author-featured p{font-size:13.4px;line-height:24px}
.author-featured span{font-size:13px;text-decoration:underline}
.btn-red{background:var(--red);color:var(--white);font-weight:600;font-size:16px;display:flex;align-items:center;justify-content:center}
.view-all{left:491px;top:1789px;width:218px;height:38px}

/* news */
.news{left:0;top:1912px;width:1200px;height:473px;background:var(--grey-bg)}
.news-title{top:80px}
.news-rule{left:555px;top:130px}
.news-card{top:168px;width:501px;height:218px;background:var(--white);box-shadow:0 2px 6px rgba(0,0,0,.12)}
.date{left:0;top:0;width:66px;height:56px}
.date-day{height:28px;background:var(--red);color:var(--white);font-size:15px;font-weight:500;display:flex;align-items:center;justify-content:center}
.date-month{height:28px;background:var(--dark);color:var(--white);font-size:15px;display:flex;align-items:center;justify-content:center}
.news-head{left:92px;top:12px;font-size:22px;font-weight:400;color:var(--ink)}
.news-line{left:66px;top:56px;width:435px;height:1px;background:#dddddd}
.news-body{left:28px;top:78px;width:450px;font-size:13.2px;line-height:25px;color:#444}

/* contact */
.contact{left:0;top:2385px;width:1200px;height:557px;background:linear-gradient(180deg,#2e3540 0%,#4d5560 45%,#3a3f46 75%,#2a2a2c 100%)}
.contact-mark{left:570px;top:40px;width:60px;height:60px;border-radius:50%;background:var(--red);border:3px solid var(--white)}
.contact-title{top:162px;color:var(--white);font-size:31px;font-weight:700}
.contact-rule{left:555px;top:212px;background:var(--red)}
.contact-sub{top:240px;color:var(--white);font-size:13.5px}
.field{border:1px solid var(--white);color:var(--white);font-size:12.5px;padding:8px 14px;background:rgba(255,255,255,.04)}
.f-name{left:86px;top:285px;width:501px;height:38px}
.f-mail{left:613px;top:285px;width:501px;height:38px}
.f-msg{left:86px;top:355px;width:1028px;height:78px}
.submit{left:491px;top:461px;width:218px;height:38px}

/* footer */
.site-footer{left:0;top:2942px;width:1200px;height:73px;background:var(--white);font-size:13px;color:#444}
.foot-contact{left:86px;top:28px;display:flex;align-items:center;gap:8px}
.foot-copy{left:610px;top:28px}
.social{right:86px;top:24px;display:flex;gap:16px}
.social span{width:18px;height:18px;border-radius:50%;background:var(--ink)}
.social span.on{background:var(--red)}
</style>
</head>
<body>

<header class="site-header abs">
  <div class="brand abs"><span class="brand-dot"></span><span class="brand-name">Beacon Point Publishing</span></div>
  <nav class="main-nav abs">
    <a href="#">Home</a><a href="#">About BPP</a><a href="#">Apply Now</a><a href="#">BPP Worlds</a><a href="#">BPP Authors</a><a href="#">FAQ</a><a href="#">News</a><a href="#">Contact us</a>
  </nav>
</header>

<section class="hero abs" role="img" aria-label="Stack of open books on a white wooden table"></section>
<h1 class="hero-title abs">LOREM IPSUM SIMPLE</h1>
<div class="hero-video abs" role="img" aria-label="Video still of a person reading a book">
  <svg class="play abs" viewBox="0 0 78 78"><circle cx="39" cy="39" r="36" fill="none" stroke="#fff" stroke-width="4"/><path d="M31 24 L56 39 L31 54 Z" fill="none" stroke="#fff" stroke-width="4" stroke-linejoin="round"/></svg>
</div>
<div class="hero-apply abs">Apply Now</div>

<section>
  <h2 class="sec-title about-title abs">About BPP</h2>
  <div class="rule about-rule abs"></div>
  <p class="about-text abs">Contrary to popular belief, Lorem Ipsum is not simply random text. It has roots in a piece of classical Latin literature from 45 BC, making it over 2000 years old. Daniel Harrow, a Latin professor at Westbrook College in Vermont, looked up one of the more obscure Latin words, consectetur, from a Lorem Ipsum passage, and going through the cites of the word in classical literature, discovered the undoubtable source... <span class="more">READ MORE</span></p>
</section>

<section class="worlds abs">
  <div class="worlds-img abs" role="img" aria-label="Photo of a glowing globe rising from open book pages"></div>
  <div class="worlds-box abs">
    <h2>BPP WORLDS</h2>
    <div class="rule"></div>
    <p>Contrary to popular belief, Lorem Ipsum is not simply random text. It has roots in a piece of classical Latin literature from 45 BC, making it over 2000 years old.</p>
    <div class="btn-white">Check Now</div>
  </div>
</section>

<section>
  <h2 class="sec-title center authors-title abs">BPP Authors</h2>
  <div class="rule authors-rule abs"></div>
  <div class="author author-featured abs" style="left:86px">
    <h3>JOHN DOE</h3>
    <p>Lorem Ipsum is not simply random text. it has roots in a piece of classical Latin literature from 45 BC, making it over 2000 years old.</p>
    <span>VIEW DETAILS</span>
  </div>
  <div class="author author-photo abs" style="left:350px" role="img" aria-label="Portrait of an author"><div class="author-name abs">JOHN DOE</div></div>
  <div class="author author-photo abs" style="left:613px" role="img" aria-label="Portrait of an author"><div class="author-name abs">JOHN DOE</div></div>
  <div class="author author-photo abs" style="left:877px" role="img" aria-label="Portrait of an author"><div class="author-name abs">JOHN DOE</div></div>
  <div class="btn-red view-all abs">View All</div>
</section>

<section class="news abs">
  <h2 class="sec-title center news-title abs">Latest News</h2>
  <div class="rule news-rule abs"></div>
  <article class="news-card abs" style="left:86px">
    <div class="date abs"><div class="date-day">20th</div><div class="date-month">July</div></div>
    <h3 class="news-head abs">Lorem ipsum simply dummy text...</h3>
    <div class="news-line abs"></div>
    <p class="news-body abs">It is a long established fact that a reader will be distracted by the readable content of a page when looking at its layout. The point of using Lorem Ipsum is that it has a more-or-less normal distribution of letters, as opposed to using 'Content here, content here', making it look like readable English... <span class="more">READ MORE</span></p>
  </article>
  <article class="news-card abs" style="left:613px">
    <div class="date abs"><div class="date-day">20th</div><div class="date-month">July</div></div>
    <h3 class="news-head abs">Lorem ipsum simply dummy text...</h3>
    <div class="news-line abs"></div>
    <p class="news-body abs">It is a long established fact that a reader will be distracted by the readable content of a page when looking at its layout. The point of using Lorem Ipsum is that it has a more-or-less normal distribution of letters, as opposed to using 'Content here, content here', making it look like readable English... <span class="more">READ MORE</span></p>
  </article>
</section>

<section class="contact abs" role="img" aria-label="Rocket launching above the clouds">
  <div class="contact-mark abs"></div>
  <h2 class="contact-title center abs">CONTACT US</h2>
  <div class="rule contact-rule abs"></div>
  <p class="contact-sub center abs">Fill this form to contact with us:</p>
  <div class="field f-name abs">Full Name</div>
  <div class="field f-mail abs">Email</div>
  <div class="field f-msg abs">Message</div>
  <div class="btn-red submit abs">Submit</div>
</section>

<footer class="site-footer abs">
  <div class="foot-contact abs">
    <svg width="12" height="12" viewBox="0 0 24 24"><path d="M6.6 10.8a15 15 0 0 0 6.6 6.6l2.2-2.2a1 1 0 0 1 1-.25 11.4 11.4 0 0 0 3.6.57 1 1 0 0 1 1 1V20a1 1 0 0 1-1 1A17 17 0 0 1 3 4a1 1 0 0 1 1-1h3.5a1 1 0 0 1 1 1c0 1.25.2 2.45.57 3.6a1 1 0 0 1-.25 1z" fill="#ec1f27"/></svg>
    <span>0123 456 789</span><span>&nbsp;|&nbsp;</span>
    <svg width="13" height="10" viewBox="0 0 26 20"><rect width="26" height="20" rx="2" fill="#ec1f27"/><path d="M1 2 L13 11 L25 2" stroke="#fff" stroke-width="2" fill="none"/></svg>
    <span>info@beaconpointpublishing.com</span>
  </div>
  <div class="foot-copy abs">© Copyright 2018 &nbsp;|&nbsp; All Rights Reserved.</div>
  <div class="social abs"><span aria-label="Social link"></span><span class="on" aria-label="Social link"></span><span aria-label="Social link"></span></div>
</footer>

</body>
</html>
```